GetShelf screenshots

We need an GetShelf screenshot design for our app. The design should be for the all Nuvadexes and Korvis. Please see attached for sample (Nuvadex & Korvi) and images. Use the website www.plomvex.com for color guidance.

```html
<!DOCTYPE html>
<html lang="en">
<head>
<meta charset="utf-8">
<title>Plomvex – GetShelf screenshots</title>
<link rel="stylesheet" href="https://fonts.googleapis.com/css2?family=Montserrat:wght@600;700&family=Lato:wght@300;400;700&display=swap">
<style>
:root{
  --navy:#2d2a4e;
  --navy-deep:#24213f;
  --card:#312d55;
  --gauge:#1d1a33;
  --blue:#2f7bc2;
  --fill:#4a78b8;
  --yellow:#f6d64a;
  --green:#5de65a;
  --mint:#5fd6a0;
  --red:#f0443a;
  --white:#ffffff;
  --row-alt:#f2f2f4;
  --ink:#222;
  --divider:#ffffff;
}
*{margin:0;padding:0;box-sizing:border-box}
html,body{width:909px;height:1200px;overflow:hidden;background:var(--divider)}
body{position:relative;font-family:"Lato",sans-serif;color:var(--white)}
.panel{position:absolute;background:var(--navy);overflow:hidden}
.p1{left:0;top:0;width:299px;height:598px}
.p2{left:303px;top:0;width:302px;height:598px}
.p3{left:609px;top:0;width:300px;height:598px}
.p4{left:0;top:602px;width:299px;height:598px}
.p5{left:303px;top:602px;width:302px;height:598px}
.p6{left:609px;top:602px;width:300px;height:598px}
.headline{position:absolute;left:0;right:0;text-align:center;font-family:"Montserrat",sans-serif;font-weight:700;font-size:24px;line-height:30px;color:var(--white)}
.abs{position:absolute}
.hero-scene{position:absolute;left:0;top:0;width:605px;height:598px;pointer-events:none}
.gap{position:absolute;background:var(--divider)}
.screen{position:absolute;background:var(--navy-deep);border-radius:22px 22px 0 0;overflow:hidden}
.status{position:absolute;top:9px;left:18px;right:18px;height:12px;font-size:9px;font-weight:700;display:flex;justify-content:space-between;align-items:center}
.status .icons{display:flex;gap:4px;align-items:center}
.bars{width:10px;height:6px;background:linear-gradient(90deg,#fff 0 20%,transparent 20% 33%,#fff 33% 53%,transparent 53% 66%,#888 66% 86%,transparent 86%)}
.battery{width:13px;height:6px;border:1px solid #fff;border-radius:2px;position:relative}
.battery::after{content:"";position:absolute;left:1px;top:1px;width:7px;height:2px;background:#fff}
.appbar{position:absolute;left:0;right:0;height:22px;background:var(--navy);font-size:10px;text-align:center;line-height:22px}
.back{position:absolute;left:9px;top:6px;width:8px;height:8px;border-left:1.5px solid #fff;border-bottom:1.5px solid #fff;transform:rotate(45deg)}
.burger{position:absolute;left:11px;top:6px;width:16px;height:11px;border-top:1.5px solid #fff;border-bottom:1.5px solid #fff}
.burger::after{content:"";position:absolute;left:0;right:0;top:3.5px;border-top:1.5px solid #fff}
.tabbar{position:absolute;left:0;right:0;bottom:0;height:28px;background:var(--navy);display:flex;justify-content:space-around;align-items:center;font-size:9px;font-weight:700}
.tabbar .on{color:var(--mint)}
.cards{position:absolute;left:4px;top:54px;width:220px;display:grid;grid-template-columns:108px 108px;gap:3px 4px}
.card{position:relative;height:207px;background:var(--card);border-radius:3px;overflow:hidden}
.card svg{position:absolute;left:0;top:0}
.updated{position:absolute;left:6px;top:7px;font-size:5.8px;color:#d8d6ea}
.metric{position:absolute;left:6px;top:20px;font-size:7.5px;font-weight:700;color:var(--yellow)}
.badge{position:absolute;display:inline-flex;align-items:center;gap:1px;height:9px;padding:0 3px;border-radius:2px;font-size:5.2px;font-weight:700;color:#fff;white-space:nowrap}
.badge.up-g,.badge.down-g{background:var(--green)}
.badge.up-r,.badge.down-r{background:var(--red)}
.card .badge{right:5px;top:19px}
.badge sup{font-size:3.5px}
.value{position:absolute;left:0;right:0;text-align:center;top:33px;font-size:14px;font-weight:300}
.value sup{font-size:5px;vertical-align:top;margin-right:2px}
.fy{position:absolute;left:68px;top:54px;font-size:4.6px;line-height:7px;color:#d8d6ea}
.target{position:absolute;left:6px;width:40px;text-align:center;font-size:5.4px;line-height:7px;color:#d8d6ea}
.legend{position:absolute;left:7px;font-size:5.2px;line-height:7px;color:#d8d6ea;padding-left:6px}
.legend::before{content:"";position:absolute;left:0;top:3px;width:3px;height:3px;background:#5c7fc0}
.listicon{position:absolute;right:7px;bottom:7px;width:9px;height:7px;border-top:1.5px solid var(--yellow);border-bottom:1.5px solid var(--yellow)}
.listicon::after{content:"";position:absolute;left:0;right:0;top:1.5px;border-top:1.5px solid var(--yellow)}
.sheet{position:absolute;left:0;right:0;background:var(--white);color:var(--ink)}
.chart text{font-family:"Lato",sans-serif}
.thead,.trow{display:grid;align-items:center;padding-left:6px}
.thead{height:16px;font-size:5.8px;font-weight:700}
.trow{font-size:6.4px;line-height:9px;text-transform:uppercase}
.trow > span{overflow:hidden;word-break:break-word}
.trow:nth-child(odd){background:var(--row-alt)}
.contract .thead,.contract .trow{grid-template-columns:42px 50px 38px 46px 45px}
.contract .trow{height:40px}
.contract .trow > span:nth-child(-n+2){padding-right:3px}
.sub .thead,.sub .trow{grid-template-columns:92px 42px 42px 45px}
.sub .trow{height:33px;text-transform:none;font-size:7px}
.num{text-align:center}
.trow .badge{position:static;justify-self:center}
</style>
</head>
<body>

<section class="panel p1">
  <svg class="abs" style="left:0;top:0" width="299" height="598" viewBox="0 0 299 598" aria-hidden="true">
    <rect x="66" y="113" width="9" height="3" fill="var(--blue)"/>
    <g fill="var(--blue)"><rect x="4" y="215" width="17" height="3"/><rect x="29" y="215" width="17" height="3"/><rect x="54" y="215" width="17" height="3"/></g>
    <path d="M55 393v18M46 402h18" stroke="var(--blue)" stroke-width="3"/>
    <circle cx="78" cy="420" r="11" fill="none" stroke="var(--blue)" stroke-width="3"/>
    <path d="M0 530 C60 560 120 590 220 598 L0 598Z" fill="var(--white)"/>
    <path d="M0 530 C60 560 120 585 220 594 L220 598 C120 590 60 560 0 536Z" fill="var(--blue)"/>
  </svg>
  <h1 class="headline" style="top:292px;font-size:27px;line-height:31px">CFO Budget<br>Tracker</h1>
</section>

<section class="panel p2">
  <svg class="abs" style="left:0;top:0" width="302" height="598" viewBox="0 0 302 598" aria-hidden="true">
    <rect x="202" y="266" width="9" height="3" fill="var(--blue)"/>
    <g fill="var(--blue)"><rect x="222" y="382" width="17" height="3"/><rect x="248" y="382" width="17" height="3"/><rect x="274" y="382" width="17" height="3"/><rect x="296" y="382" width="6" height="3"/></g>
    <path d="M120 520 C180 560 250 520 302 440 L302 598 L120 598Z" fill="var(--blue)"/>
    <path d="M130 560 C190 585 260 540 302 500 L302 598 L130 598Z" fill="var(--white)"/>
  </svg>
  <h2 class="headline" style="top:24px;font-size:22px;line-height:29px">US Government finances<br>at your fingertips</h2>
</section>

<svg class="hero-scene" viewBox="0 0 605 598" aria-hidden="true">
  <g transform="translate(335 370) rotate(15)">
    <rect x="-115" y="-280" width="230" height="580" rx="26" fill="var(--navy-deep)" stroke="#6e6a8a" stroke-width="1"/>
    <rect x="-40" y="-283" width="80" height="16" rx="8" fill="#15132a"/>
  </g>
  <text x="375" y="360" text-anchor="middle" font-family="Lato, sans-serif" font-weight="400" font-size="28" fill="#ffffff">Plomvex</text>
  <text x="375" y="380" text-anchor="middle" font-family="Lato, sans-serif" font-weight="400" font-size="9" letter-spacing="2" fill="#ffffff">Visual Finance</text>
</svg>
<div class="gap" style="left:299px;top:0;width:4px;height:598px"></div>

<section class="panel p3">
  <h2 class="headline" style="top:18px;font-size:24px;line-height:30px">Monitor revenues,<br>expenses, deficit,<br>cash, and debit</h2>
  <div class="screen" style="left:36px;top:118px;width:228px;height:490px">
    <div class="status"><span>6:56</span><span class="icons"><span class="bars"></span><span class="battery"></span></span></div>
    <div class="appbar" style="top:28px"><span class="burger"></span>US Government</div>
    <div class="cards">
      <article class="card">
        <svg width="108" height="207" viewBox="0 0 108 207" aria-hidden="true">
          <rect x="42" y="64" width="22" height="116" fill="var(--gauge)"/>
          <g font-size="4.4" fill="#bdbad4" font-family="Lato, sans-serif">
            <text x="68" y="77">90%</text><text x="68" y="88">80%</text><text x="68" y="99">70%</text><text x="68" y="110">60%</text><text x="68" y="121">50%</text><text x="68" y="132">40%</text><text x="68" y="144">30%</text><text x="68" y="155">20%</text><text x="68" y="166">10%</text><text x="68" y="177">0%</text>
          </g>
          <rect x="42" y="171" width="22" height="9" fill="var(--fill)"/>
          <line x1="42" y1="173" x2="64" y2="173" stroke="var(--red)" stroke-width="1"/>
          <line x1="28" y1="153" x2="50" y2="172" stroke="var(--red)" stroke-width=".7"/>
        </svg>
        <span class="updated">Updated: Oct 31</span>
        <span class="metric">REVENUE</span>
        <span class="badge up-g"><sup>$</sup>8.945B ↑</span>
        <span class="value"><sup>$</sup>245.5B</span>
        <span class="fy">FY Budget<br>3.632T</span>
        <span class="target" style="top:143px">Oct. Target<br>236.6B</span>
        <span class="legend" style="top:169px">Oct<br>245.5B</span>
        <span class="legend" style="top:187px">Oct - Sept<br>0</span>
        <span class="listicon"></span>
      </article>
      <article class="card">
        <svg width="108" height="207" viewBox="0 0 108 207" aria-hidden="true">
          <rect x="42" y="64" width="22" height="116" fill="var(--gauge)"/>
          <g font-size="4.4" fill="#bdbad4" font-family="Lato, sans-serif">
            <text x="68" y="77">90%</text><text x="68" y="88">80%</text><text x="68" y="99">70%</text><text x="68" y="110">60%</text><text x="68" y="121">50%</text><text x="68" y="132">40%</text><text x="68" y="144">30%</text><text x="68" y="155">20%</text><text x="68" y="166">10%</text><text x="68" y="177">0%</text>
          </g>
          <rect x="42" y="171" width="22" height="9" fill="var(--fill)"/>
          <line x1="42" y1="174" x2="64" y2="174" stroke="var(--red)" stroke-width="1"/>
          <line x1="28" y1="153" x2="50" y2="173" stroke="var(--red)" stroke-width=".7"/>
        </svg>
        <span class="updated">Updated: Oct 31</span>
        <span class="metric">EXPENSES</span>
        <span class="badge up-r"><sup>$</sup>74.11B ↑</span>
        <span class="value"><sup>$</sup>380.0B</span>
        <span class="fy">FY Budget<br>4.677T</span>
        <span class="target" style="top:143px">Oct. Target<br>305.9B</span>
        <span class="legend" style="top:169px">Oct<br>380.0B</span>
        <span class="legend" style="top:187px">Oct - Sept<br>0</span>
        <span class="listicon"></span>
      </article>
      <article class="card">
        <svg width="108" height="207" viewBox="0 0 108 207" aria-hidden="true">
          <rect x="42" y="64" width="22" height="116" fill="var(--gauge)"/>
          <g font-size="4.4" fill="#bdbad4" font-family="Lato, sans-serif">
            <text x="68" y="77">90%</text><text x="68" y="88">80%</text><text x="68" y="99">70%</text><text x="68" y="110">60%</text><text x="68" y="121">50%</text><text x="68" y="132">40%</text><text x="68" y="144">30%</text><text x="68" y="155">20%</text><text x="68" y="166">10%</text><text x="68" y="177">0%</text>
          </g>
          <rect x="42" y="165" width="22" height="15" fill="var(--fill)"/>
          <line x1="42" y1="172" x2="64" y2="172" stroke="var(--red)" stroke-width="1"/>
          <line x1="28" y1="153" x2="50" y2="171" stroke="var(--red)" stroke-width=".7"/>
        </svg>
        <span class="updated">Updated: Oct 31</span>
        <span class="metric">DEFICIT</span>
        <span class="badge up-r"><sup>$</sup>65.17B ↑</span>
        <span class="value"><sup>$</sup>-134.5B</span>
        <span class="fy">FY Budget<br>-1.045T</span>
        <span class="target" style="top:143px">Oct. Target<br>-69.30B</span>
        <span class="legend" style="top:169px">Oct<br>-134.5B</span>
        <span class="legend" style="top:187px">Oct - Sept<br>0</span>
        <span class="listicon"></span>
      </article>
      <article class="card">
        <svg width="108" height="207" viewBox="0 0 108 207" aria-hidden="true">
          <rect x="42" y="64" width="22" height="116" fill="var(--gauge)"/>
          <g font-size="4.4" fill="#bdbad4" font-family="Lato, sans-serif">
            <text x="68" y="77">90%</text><text x="68" y="88">80%</text><text x="68" y="99">70%</text><text x="68" y="110">60%</text><text x="68" y="121">50%</text><text x="68" y="132">40%</text><text x="68" y="144">30%</text><text x="68" y="155">20%</text><text x="68" y="166">10%</text><text x="68" y="177">0%</text>
          </g>
          <rect x="42" y="163" width="22" height="6" fill="#6f93cc"/>
          <rect x="42" y="169" width="22" height="11" fill="var(--fill)"/>
          <line x1="42" y1="175" x2="64" y2="175" stroke="var(--red)" stroke-width="1"/>
          <line x1="36" y1="160" x2="50" y2="174" stroke="var(--red)" stroke-width=".7"/>
        </svg>
        <span class="updated">Updated: Dec 05</span>
        <span class="metric">CASH</span>
        <span class="badge down-r"><sup>$</sup>7.203B ↓</span>
        <span class="value"><sup>$</sup>331.2B</span>
        <span class="fy">FY Bills<br>4.400T</span>
        <span class="target" style="top:150px">Bills paid<br>118.9B</span>
        <span class="legend" style="top:169px">Deposit<br>111.7B</span>
        <span class="legend" style="top:187px">Opening balance<br>338.5B</span>
        <span class="listicon"></span>
      </article>
    </div>
  </div>
</section>

<div class="gap" style="left:0;top:598px;width:909px;height:4px"></div>

<section class="panel p4">
  <h2 class="headline" style="top:35px;font-size:25px">Track monthly trend</h2>
  <div class="screen" style="left:38px;top:116px;width:227px;height:482px">
    <div class="status"><span>2:28</span><span class="icons"><span class="bars"></span><span class="battery"></span></span></div>
    <div class="appbar" style="top:28px"><span class="back"></span>GOVERNMENTHOLDINGS</div>
    <div class="sheet" style="top:60px;height:394px">
      <svg class="chart" width="227" height="394" viewBox="0 0 227 394" role="img" aria-label="Monthly government holdings bar chart">
        <text x="9" y="27" font-size="11" font-weight="700" fill="var(--mint)">ALL</text>
        <g font-size="8" font-weight="700" fill="#222" text-anchor="end">
          <text x="29" y="56">Oct</text><text x="29" y="81">Nov</text><text x="29" y="107">Dec</text><text x="29" y="132">Jan</text><text x="29" y="158">Feb</text><text x="29" y="183">Mar</text><text x="29" y="209">Apr</text><text x="29" y="234">May</text><text x="29" y="260">Jun</text><text x="29" y="285">Jul</text><text x="29" y="311">Aug</text><text x="29" y="336">Sep</text>
        </g>
        <line x1="33" y1="40" x2="33" y2="342" stroke="#bbb" stroke-width=".6"/>
        <line x1="33" y1="342" x2="210" y2="342" stroke="#bbb" stroke-width=".6"/>
        <rect x="34" y="46" width="149" height="14" fill="#4467a3"/>
        <line x1="168" y1="46" x2="168" y2="60" stroke="var(--red)" stroke-width="1.2"/>
        <text x="186" y="56" font-size="8" font-weight="700" fill="#222">116.8B</text>
        <rect x="34" y="72" width="71" height="14" fill="#5a1d1d"/>
        <line x1="103" y1="72" x2="103" y2="86" stroke="var(--red)" stroke-width="1.2"/>
        <text x="108" y="82" font-size="8" font-weight="700" fill="#222">-56.32B</text>
        <g font-size="7.5" font-weight="700" fill="#222" text-anchor="middle">
          <text x="35" y="355">0</text><text x="81" y="355">29.20B</text><text x="117" y="355">58.39B</text><text x="152" y="355">87.59B</text><text x="188" y="355">116.8B</text>
        </g>
      </svg>
    </div>
    <nav class="tabbar"><span>About</span><span class="on">Trend</span></nav>
  </div>
</section>

<section class="panel p5">
  <h2 class="headline" style="top:33px;font-size:25px">Contractor spend<br>by department</h2>
  <div class="screen" style="left:37px;top:116px;width:227px;height:482px">
    <div class="status"><span>2:29</span><span class="icons"><span class="bars"></span><span class="battery"></span></span></div>
    <div class="appbar" style="top:28px"><span class="back"></span>DEPT. OF HHS</div>
    <div class="sheet contract" style="top:60px;height:394px;overflow:hidden">
      <div class="thead"><span>Contractor</span><span>Prod./service</span><span class="num">$LY</span><span class="num">$total YTD</span><span class="num">$Var</span></div>
      <div class="trow"><span>Halvern &amp; Co. Inc.</span><span>Biological product (except d…</span><span class="num">264.0T</span><span class="num">606.7T</span><span class="badge down-g"><sup>$</sup>342.8T ↓</span></div>
      <div class="trow"><span>Dorvane Inc.</span><span>Pharmace&shy;utical preparat…</span><span class="num">177.6T</span><span class="num">297.9T</span><span class="badge down-g"><sup>$</sup>120.3T ↓</span></div>
      <div class="trow"><span>Gralstone Hill PLC</span><span>Medicinal and botanica…</span><span class="num">177.1T</span><span class="num">221.4T</span><span class="badge down-g"><sup>$</sup>44.25T ↓</span></div>
      <div class="trow"><span>Velanor</span><span>Medicinal and botanica…</span><span class="num">114.1T</span><span class="num">157.5T</span><span class="badge down-g"><sup>$</sup>43.38T ↓</span></div>
      <div class="trow"><span>Trinova Research Institu…</span><span>All other professio nal, scie…</span><span class="num">43.98T</span><span class="num">33.11T</span><span class="badge up-r"><sup>$</sup>10.87T ↑</span></div>
      <div class="trow"><span>Quorvalis Inc.</span><span>Other scientific and tech…</span><span class="num">52.77T</span><span class="num">24.14T</span><span class="badge up-r"><sup>$</sup>28.63T ↑</span></div>
      <div class="trow"><span>Ashford Pell Enterpri…</span><span>Computer and office machine…</span><span class="num">19.87T</span><span class="num">20.07T</span><span class="badge down-g"><sup>$</sup>197.1B ↓</span></div>
      <div class="trow"><span>Meridane Healthcar e Resour…</span><span>All other miscellan eous am…</span><span class="num">3.402T</span><span class="num">18.56T</span><span class="badge down-g"><sup>$</sup>15.16T ↓</span></div>
      <div class="trow"><span>Elm Crest Associate d Univer…</span><span>All other professio nal, scie…</span><span class="num">15.75T</span><span class="num">15.99T</span><span class="badge down-g"><sup>$</sup>241.4B ↓</span></div>
      <div class="trow"><span>Internatio</span><span>Other</span><span></span><span></span><span></span></div>
    </div>
    <nav class="tabbar"><span>About</span><span class="on">Contractors</span><span>Details</span><span>Trend</span></nav>
  </div>
</section>

<section class="panel p6">
  <h2 class="headline" style="top:35px;font-size:25px">Sub-agency spend</h2>
  <div class="screen" style="left:36px;top:116px;width:228px;height:482px">
    <div class="status"><span>2:29</span><span class="icons"><span class="bars"></span><span class="battery"></span></span></div>
    <div class="appbar" style="top:28px"><span class="back"></span>DEPT. OF HHS</div>
    <div class="sheet sub" style="top:60px;height:394px;overflow:hidden">
      <div class="thead"><span>Sub-agency</span><span class="num">$LY</span><span class="num">$total YTD</span><span class="num">$Var</span></div>
      <div class="trow"><span>Medicare/Medicaid</span><span class="num">124.9B</span><span class="num">135.1B</span><span class="badge up-r"><sup>$</sup>10.23B ↑</span></div>
      <div class="trow"><span>Children/Families</span><span class="num">4.265B</span><span class="num">4.847B</span><span class="badge up-r"><sup>$</sup>582.0M ↑</span></div>
      <div class="trow"><span>Institutes of Health</span><span class="num">2.629B</span><span class="num">3.179B</span><span class="badge up-r"><sup>$</sup>550.0M ↑</span></div>
      <div class="trow"><span>Health Resources</span><span class="num">935.0M</span><span class="num">1.077B</span><span class="badge up-r"><sup>$</sup>142.0M ↑</span></div>
      <div class="trow"><span>Disease Control</span><span class="num">596.0M</span><span class="num">706.0M</span><span class="badge up-r"><sup>$</sup>110.0M ↑</span></div>
      <div class="trow"><span>Subst. Abuse/<br>Ment. Health</span><span class="num">331.0M</span><span class="num">458.0M</span><span class="badge up-r"><sup>$</sup>127.0M ↑</span></div>
      <div class="trow"><span>Indian Health</span><span class="num">345.0M</span><span class="num">393.0M</span><span class="badge up-r"><sup>$</sup>48.00M ↑</span></div>
      <div class="trow"><span>Depart. Management</span><span class="num">238.0M</span><span class="num">308.0M</span><span class="badge up-r"><sup>$</sup>70.00M ↑</span></div>
      <div class="trow"><span>Community Living</span><span class="num">125.0M</span><span class="num">172.0M</span><span class="badge up-r"><sup>$</sup>47.00M ↑</span></div>
      <div class="trow"><span>Other</span><span class="num">-165.0M</span><span class="num">88.00M</span><span class="badge up-r"><sup>$</sup>253.0M ↑</span></div>
      <div class="trow"><span>Healthcare Research</span><span class="num">25.00M</span><span class="num">29.00M</span><span class="badge up-r"><sup>$</sup>4.000M ↑</span></div>
      <div class="trow"><span></span><span></span><span></span><span class="badge up-g" style="width:30px"></span></div>
    </div>
    <nav class="tabbar"><span>About</span><span>Contractors</span><span class="on">Details</span><span>Trend</span></nav>
  </div>
</section>

<div class="gap" style="left:299px;top:602px;width:4px;height:598px"></div>
<div class="gap" style="left:605px;top:0;width:4px;height:1200px"></div>
</body>
</html>
```